Corporate Design für Kaltakquise und Vertrieb in Kooperation im BtoB
Zielgruppe
Zielgruppe sind Unternehmen im BtoB Bereich, wir sind ein Outsouring Büro für Kaltakquise, Vertrieb - ausschließlich im BtoB Bereich, wir öffnen die Türen zu potentiellen Kunden, arrangieren Vorträge bei einschlägigen Kongressen um neie Kunden zu generieren, den Termin vor Ort nimmt der Partner wahr, wir betreuen den Kunden im After Sales Bereich
Aufgabenstellung
markant und einprägsam, geradlinig, nicht verschnörkelt professionell - dynamisch und powerfull

```html
<!DOCTYPE html>
<html lang="de">
<head>
<meta charset="utf-8">
<title>kovantis – Corporate Design</title>
<link href="https://fonts.googleapis.com/css2?family=Ubuntu:wght@400;500&family=Open+Sans:wght@600&display=swap" rel="stylesheet">
<style>
  :root {
    --brand-red: #cb1a20;
    --brand-grey: #58585a;
    --text-grey: #55565a;
    --paper: #ffffff;
    --panel-grey: #e6e6e8;
    --stage-top: #e8e8ea;
    --stage-bottom: #bcc0c4;
  }
  * { margin: 0; padding: 0; box-sizing: border-box; }
  html, body { width: 754px; height: 1200px; overflow: hidden; }
  body {
    position: relative;
    background: var(--paper);
    font-family: "Ubuntu", sans-serif;
    color: var(--text-grey);
  }
  address { font-style: normal; }
  .wordmark {
    font-family: "Ubuntu", sans-serif;
    font-weight: 500;
    color: var(--brand-grey);
    letter-spacing: 0.02em;
    line-height: 1;
    white-space: nowrap;
  }
  .hero-logo {
    position: absolute;
    left: 0; right: 0; top: 128px;
    text-align: center;
    font-size: 108px;
  }
  .stationery {
    position: absolute;
    left: 0; top: 354px;
    width: 754px; height: 846px;
    background: linear-gradient(var(--stage-top), var(--stage-bottom));
  }
  .sheet, .card {
    position: absolute;
    background: var(--paper);
    box-shadow: 4px 5px 8px rgba(0,0,0,0.18);
    overflow: hidden;
  }
  .contact-panel {
    position: absolute;
    right: 0; bottom: 0;
    background: var(--panel-grey);
  }

  .letterhead { left: 231px; top: 79px; width: 479px; height: 678px; }
  .letterhead .contact-panel { width: 112px; height: 128px; }
  .letterhead .wordmark { position: absolute; left: 309px; top: 44px; font-size: 27px; }
  .letterhead-contact {
    position: absolute; left: 390px; top: 576px;
    font-size: 7.6px; line-height: 11px;
  }
  .letterhead-contact .company { color: var(--brand-red); }
  .letterhead-contact .gap { margin-top: 6px; }
  .accent { color: var(--brand-red); }

  .card-front { left: 41px; top: 280px; width: 242px; height: 157px; }
  .card-front .contact-panel { width: 92px; height: 70px; }
  .card-front .wordmark { position: absolute; left: 15px; top: 19px; font-size: 24px; }
  .person-name {
    position: absolute; left: 21px; top: 94px;
    font-size: 9.4px; color: var(--brand-red);
  }
  .person-address {
    position: absolute; left: 21px; top: 121px;
    font-size: 7.4px; line-height: 11px;
  }
  .card-contact {
    position: absolute; right: 15px; top: 96px;
    text-align: right; font-size: 7.4px; line-height: 11px;
  }

  .card-back {
    left: 40px; top: 458px; width: 242px; height: 156px;
    background: var(--brand-red);
  }
  .card-back .web {
    position: absolute; left: 0; right: 0; top: 96px;
    text-align: center;
    font-family: "Open Sans", sans-serif; font-weight: 600;
    font-size: 15px; color: var(--paper);
  }
</style>
</head>
<body>
  <header class="hero-logo wordmark">kovantis</header>

  <section class="stationery">
    <article class="sheet letterhead">
      <div class="contact-panel" role="img" aria-label="Graue Fläche hinter den Kontaktdaten"></div>
      <div class="wordmark">kovantis</div>
      <address class="letterhead-contact">
        <div class="company">KOVANTIS</div>
        <div>Beispielweg 8</div>
        <div>54321 Hamburg</div>
        <div class="gap">T: 040 / 9 87 65 43</div>
        <div>F: 040 / 9 87 65 43</div>
        <div>info@kovantis.com</div>
        <div class="accent">www.kovantis.com</div>
      </address>
    </article>

    <article class="card card-front">
      <div class="contact-panel" role="img" aria-label="Graue Fläche hinter den Kontaktdaten"></div>
      <div class="wordmark">kovantis</div>
      <div class="person-name">Lena Beispiel</div>
      <address class="person-address">
        <div>Beispielweg 8</div>
        <div>54321 Hamburg</div>
      </address>
      <address class="card-contact">
        <div>T: 040 / 9 87 65 43</div>
        <div>F: 040 / 9 87 65 43</div>
        <div>info@vendura.com</div>
        <div class="accent">www.vendura.com</div>
      </address>
    </article>

    <article class="card card-back">
      <div class="web">www.kovantis.com</div>
    </article>
  </section>
</body>
</html>
```